"Thank You" card for professional property management agency.

We need to create a DL size "Thank You" card primarily used to thank new clients for their business and referrals.
We are a real estate agency based on Sydney's Northern Beaches. We want the card to feel happy and professional, incorporating our logo.
See our website for details about our business - www.harbourleafrealty.com.au
We have attached our logo in black text and white text as well as some images we have used across our website.
One side must have the ability to hand write a message of thank you on.
I would like this to be a clean and simple design, feel free to use any image supplied, but we are also happy with plain or patterned designs too.

Target Market(s)

Property investors male and female aged 30-60

Industry/Entity Type

Real Estate

Font styles to use
Other font styles liked:
• Please let the designer choose font

Colors

Designer to choose colors to be used in the design.

Requirements
Must have
• DL Size: Full Bleed 213x102mm. Doc size 210x99mm (horizontal)
• Harbour Leaf Realty Logo
• Contact Details:
• info@harbourleafrealty.com.au
• Tel: 0498 217 603
• Level 2, 17 Wattlecombe Rd, Wattlecombe NSW 2187
• "Thank You" somewhere on the card
• Area or side to write message on.
• Design to be provided in editable photoshop PSD file and print ready PDF file
Nice to have
• Sleek professional design that feels "happy or grateful" as it is a thank you card
• Happy to use a plain colour or pattern on one side - it does not have to be an image provided, but feel free to design with either.
Should not have
• should not be too busy, keep it clean and simple.

```html
<!DOCTYPE html>
<html lang="en">
<head>
<meta charset="utf-8">
<title>Harbour Leaf Realty – Thank You Card</title>
<link rel="stylesheet" href="https://fonts.googleapis.com/css2?family=Roboto:wght@400;700&family=Sacramento&family=Pinyon+Script&family=Cormorant+Garamond:wght@300&display=swap">
<style>
  :root {
    --paper: #ffffff;
    --teal: #2b9fa2;
    --teal-deep: #1a7688;
    --ink: #1a1a1a;
    --sky-top: #0c4a6e;
    --sky-mid: #1e7fb8;
    --sky-low: #5db4e0;
    --water: #1f6f9c;
    --garden: #4d7a3a;
  }
  * { margin: 0; padding: 0; box-sizing: border-box; }
  html, body { width: 1200px; height: 574px; overflow: hidden; background: var(--paper); }
  .card { position: relative; width: 1200px; height: 574px; background: var(--paper); overflow: hidden; }

  .harbour-photo {
    position: absolute; left: 0; top: 0; width: 600px; height: 389px;
    background: linear-gradient(180deg, var(--sky-top) 0%, var(--sky-mid) 38%, var(--sky-low) 62%, var(--water) 66%, #2b7fa8 100%);
  }
  .teal-block {
    position: absolute; left: 273px; top: 308px; width: 327px; height: 81px;
    background: var(--teal); opacity: 0.92;
  }
  .homes-photo {
    position: absolute; left: 0; top: 389px; width: 273px; height: 185px;
    background: linear-gradient(180deg, #3b8fd0 0%, #9cc9e8 35%, #8c8e8a 60%, var(--garden) 80%, #6f6f6b 100%);
  }

  .thanks {
    position: absolute; left: 290px; top: 440px; width: 300px; height: 80px;
    display: flex; align-items: center; justify-content: space-between;
    color: var(--teal);
  }
  .thanks .brace {
    font-family: "Cormorant Garamond", serif; font-weight: 300;
    font-size: 78px; line-height: 1;
  }
  .thanks .word {
    font-family: "Pinyon Script", cursive; font-size: 38px; color: var(--teal-deep);
  }

  .brand {
    position: absolute; right: 56px; top: 94px;
    display: flex; align-items: center; gap: 10px;
  }
  .brand .mark { width: 16px; height: 16px; background: var(--teal); }
  .brand .name {
    font-family: "Roboto", sans-serif; font-weight: 700; font-size: 26px;
    color: var(--ink); text-transform: uppercase; letter-spacing: -0.3px;
  }

  .message {
    position: absolute; left: 660px; top: 226px; width: 472px;
    text-align: center; font-family: "Sacramento", cursive;
    font-size: 30px; line-height: 36px; color: var(--ink);
  }

  .contact {
    position: absolute; left: 660px; top: 450px; width: 472px;
    text-align: center; font-family: "Roboto", sans-serif;
    font-size: 12px; line-height: 14px; color: var(--teal-deep); letter-spacing: 0.2px;
    font-style: normal;
  }
  .contact .address { margin-bottom: 13px; }
</style>
</head>
<body>
  <main class="card">
    <div class="harbour-photo" role="img" aria-label="Photo of a sunny harbour bay with moored boats and waterfront homes"></div>
    <div class="teal-block"></div>
    <div class="homes-photo" role="img" aria-label="Photo of modern townhouses with terraced gardens along a street"></div>

    <div class="thanks">
      <span class="brace">{</span>
      <span class="word">Thank you</span>
      <span class="brace">}</span>
    </div>

    <div class="brand">
      <span class="mark"></span>
      <span class="name">Harbour Leaf Realty</span>
    </div>

    <p class="message">Lorem ipsum dolor sit amet, consectetur adipisicing elit, sed do eiusmod tempor incididunt ut labore et dolore magna aliqua. eos qui ratione voluptatem sequi.</p>

    <address class="contact">
      <p class="address">Level 2, 17 Wattlecombe Rd, Wattlecombe NSW 2187</p>
      <p>Tel: 0498 217 603</p>
      <p>info@harbourleafrealty.com.au</p>
    </address>
  </main>
</body>
</html>
```